Price sign

Looking for a fresh new pricing sign.. with new prices size 2ft tall x 4ft wide , express lube $40.95, automatic transmission $129.95, radiator $109.95, Torvex plus express lube $79.95, std trans/ diff $79.95, tuneup 4cyl $149.95, 6cyl $175.95 ,

```html
<!DOCTYPE html>
<html lang="en">
<head>
<meta charset="utf-8">
<title>Service Price Sign</title>
<link href="https://fonts.googleapis.com/css2?family=Anton&family=Archivo+Black&family=Kaushan+Script&display=swap" rel="stylesheet">
<style>
  :root {
    --red: #c8171e;
    --red-mid: #e2461a;
    --orange: #f28a1a;
    --amber: #f6a21c;
    --yellow: #fbd52a;
    --ink: #0d0d0d;
    --white: #ffffff;
    --brand: #c8171e;
    --chrome: linear-gradient(180deg, #ffffff 0%, #ececec 30%, #a9a9a9 48%, #5a5a5a 53%, #bdbdbd 74%, #ffffff 100%);
  }
  * { box-sizing: border-box; margin: 0; padding: 0; }
  html, body { width: 1200px; height: 600px; overflow: hidden; background: #fff; }
  .sign {
    width: 1200px; height: 600px;
    display: grid;
    grid-template-columns: repeat(3, 400px);
    grid-template-rows: repeat(2, 300px);
  }
  .panel {
    display: flex; flex-direction: column; align-items: center;
    text-align: center; overflow: hidden; padding-top: 12px;
  }
  .panel--red { background: radial-gradient(ellipse at 50% 50%, var(--amber) 0%, var(--red-mid) 45%, var(--red) 80%); }
  .panel--orange { background: radial-gradient(ellipse at 50% 55%, var(--yellow) 0%, var(--amber) 45%, var(--orange) 85%); }

  .chrome {
    font-family: "Archivo Black", sans-serif;
    background: var(--chrome);
    -webkit-background-clip: text; background-clip: text;
    color: transparent;
    filter: drop-shadow(2px 0 0 var(--ink)) drop-shadow(-2px 0 0 var(--ink)) drop-shadow(0 2px 0 var(--ink)) drop-shadow(0 -2px 0 var(--ink)) drop-shadow(2px 3px 0 var(--ink));
    line-height: 1;
  }
  .outlined {
    color: var(--white);
    text-shadow: 2px 0 0 var(--ink), -2px 0 0 var(--ink), 0 2px 0 var(--ink), 0 -2px 0 var(--ink),
                 2px 2px 0 var(--ink), -2px -2px 0 var(--ink), 2px -2px 0 var(--ink), -2px 2px 0 var(--ink);
  }
  .script-title { font-family: "Kaushan Script", cursive; font-size: 44px; line-height: 1; color: var(--white); }

  .title-lube { font-size: 76px; letter-spacing: 2px; line-height: 1.02; }
  .title-auto { font-size: 44px; line-height: 1.25; transform: scaleY(1.25); }
  .title-trans { font-size: 34px; line-height: 1.3; transform: scaleY(1.3); }
  .title-radiator { font-size: 46px; line-height: 1.2; transform: scaleY(1.15); }
  .title-service { font-size: 54px; line-height: 1.15; transform: scaleY(1.1); }
  .title-rivo { font-size: 56px; line-height: 1.12; }
  .title-tune { font-size: 52px; line-height: 1.12; }

  .service-line { font-family: "Anton", sans-serif; font-size: 29px; line-height: 1.15; margin-top: 6px; }
  .interval { font-family: "Kaushan Script", cursive; font-size: 21px; line-height: 1.25; }

  .wide {
    font-family: "Archivo Black", sans-serif; text-transform: uppercase;
    font-size: 25px; letter-spacing: 2px; line-height: 1.14;
  }
  .wide--sm { font-size: 18px; letter-spacing: 2px; }

  .price { display: flex; align-items: flex-start; justify-content: center; margin-top: 4px; }
  .price__from { font-family: "Kaushan Script", cursive; font-size: 12px; color: var(--white); margin-top: 10px; margin-right: 4px; text-shadow: 1px 1px 0 var(--ink); }
  .price__dollar { font-size: 34px; margin-top: 2px; margin-right: 4px; }
  .price__whole { font-size: 62px; letter-spacing: -1px; transform: scaleY(1.15); transform-origin: top; }
  .price__tail { display: flex; flex-direction: column; align-items: flex-start; margin-left: 6px; margin-top: 2px; }
  .price__cents { font-size: 30px; }
  .price__tax { font-family: "Kaushan Script", cursive; font-size: 13px; color: var(--ink); margin-top: 4px; margin-left: 10px; }

  .price--sm { margin-top: 2px; }
  .price--sm .price__from { font-size: 9px; margin-top: 6px; }
  .price--sm .price__dollar { font-size: 20px; margin-right: 3px; }
  .price--sm .price__whole { font-size: 34px; }
  .price--sm .price__cents { font-size: 17px; }
  .price--sm .price__tax { font-size: 8px; margin-left: 4px; margin-top: 2px; }

  .brand-row { margin: 4px 0 2px; }
  .brand-name { font-family: "Archivo Black", sans-serif; font-size: 34px; line-height: 1.1; color: var(--brand); }

  .split { display: flex; align-items: stretch; margin-top: 2px; }
  .split__option { display: flex; flex-direction: column; align-items: center; padding: 0 12px; }
  .split__divider { width: 3px; background: var(--red); margin: 4px 0; }
  .split__label { font-family: "Archivo Black", sans-serif; font-size: 17px; letter-spacing: 1px; line-height: 1.1; }

  .or-row { display: flex; align-items: center; gap: 8px; width: 290px; }
  .or-row__rule { flex: 1; height: 2px; background: var(--white); box-shadow: 0 1px 0 var(--ink); }
  .or-row__word { font-family: "Kaushan Script", cursive; font-size: 15px; line-height: 1.1; }
</style>
</head>
<body>
<main class="sign">

  <section class="panel panel--red">
    <div class="script-title outlined">Express</div>
    <div class="chrome title-lube">LUBE</div>
    <div class="service-line outlined">14 POINT SERVICE</div>
    <div class="interval outlined">Service Every 3000 Miles</div>
    <div class="price">
      <span class="price__from">From</span>
      <span class="price__dollar chrome">$</span>
      <span class="price__whole chrome">40</span>
      <span class="price__tail"><span class="price__cents chrome">95</span><span class="price__tax">plus tax</span></span>
    </div>
  </section>

  <section class="panel panel--orange">
    <div class="chrome title-auto">AUTOMATIC</div>
    <div class="chrome title-trans">TRANSMISSION</div>
    <div class="service-line outlined">30 MINUTES SERVICE</div>
    <div class="interval outlined">Service Every 25,000 Miles</div>
    <div class="price">
      <span class="price__from">From</span>
      <span class="price__dollar chrome">$</span>
      <span class="price__whole chrome">129</span>
      <span class="price__tail"><span class="price__cents chrome">95</span><span class="price__tax">plus tax</span></span>
    </div>
  </section>

  <section class="panel panel--red">
    <div class="chrome title-radiator">RADIATOR</div>
    <div class="chrome title-service">SERVICE</div>
    <div class="service-line outlined">30 MINUTES SERVICE</div>
    <div class="interval outlined">Service Every 25,000 Miles</div>
    <div class="price">
      <span class="price__from">From</span>
      <span class="price__dollar chrome">$</span>
      <span class="price__whole chrome">109</span>
      <span class="price__tail"><span class="price__cents chrome">95</span><span class="price__tax">plus tax</span></span>
    </div>
  </section>

  <section class="panel panel--orange">
    <div class="wide outlined" style="margin-top:6px">Rivo's Best</div>
    <div class="brand-row"><span class="brand-name">Torvex plus</span></div>
    <div class="wide outlined">Express Lube</div>
    <div class="service-line outlined">14 POINT SERVICE</div>
    <div class="interval outlined">Service Every 3000 Miles</div>
    <div class="price">
      <span class="price__from">From</span>
      <span class="price__dollar chrome">$</span>
      <span class="price__whole chrome">79</span>
      <span class="price__tail"><span class="price__cents chrome">95</span><span class="price__tax">plus tax</span></span>
    </div>
  </section>

  <section class="panel panel--red">
    <div class="chrome title-rivo">RIVO'S</div>
    <div class="chrome title-tune">TUNE-UP</div>
    <div class="service-line outlined">60 MINUTES SERVICE</div>
    <div class="interval outlined">Service Every 25,000 Miles</div>
    <div class="split">
      <div class="split__option">
        <span class="split__label outlined">4 CYL</span>
        <div class="price price--sm">
          <span class="price__from">From</span>
          <span class="price__dollar chrome">$</span>
          <span class="price__whole chrome">149</span>
          <span class="price__tail"><span class="price__cents chrome">95</span><span class="price__tax">plus tax</span></span>
        </div>
      </div>
      <div class="split__divider"></div>
      <div class="split__option">
        <span class="split__label outlined">6 CYL</span>
        <div class="price price--sm">
          <span class="price__from">From</span>
          <span class="price__dollar chrome">$</span>
          <span class="price__whole chrome">175</span>
          <span class="price__tail"><span class="price__cents chrome">95</span><span class="price__tax">plus tax</span></span>
        </div>
      </div>
    </div>
  </section>

  <section class="panel panel--orange">
    <div class="wide outlined" style="margin-top:2px">Standard</div>
    <div class="wide outlined">Transmission</div>
    <div class="or-row"><span class="or-row__rule"></span><span class="or-row__word outlined">Or</span><span class="or-row__rule"></span></div>
    <div class="wide outlined">Differential</div>
    <div class="wide outlined">Service</div>
    <div class="wide wide--sm outlined">15 Minutes Service</div>
    <div class="interval outlined">Service Every 25,000 Miles</div>
    <div class="price">
      <span class="price__from">From</span>
      <span class="price__dollar chrome">$</span>
      <span class="price__whole chrome">79</span>
      <span class="price__tail"><span class="price__cents chrome">95</span><span class="price__tax">plus tax</span></span>
    </div>
  </section>

</main>
</body>
</html>
```